Commercial and Multifamily informational website

We need a website for our commercial real estate management company. We will manage offices, retail, apartments and others. Here is the brief verbiage: Providing quality commercial and multifamily portfolio management to Landlords, REITs, and financial institutions. 

Industry/Entity Type

Real Estate

Number of Pages Required

2 page

Font styles to use
Sans Serif
Other font styles liked:
• Muli, Garamond

Colors
0555a3
5c5c5c
3176b5
85acd3
474747

Requirements
Must have
• Home page and contact page

```html
<!DOCTYPE html>
<html lang="en">
<head>
<meta charset="utf-8">
<title>Corvane Real Estate Management</title>
<link href="https://fonts.googleapis.com/css2?family=Arimo:wght@400;700&family=Tinos:wght@400;700&display=swap" rel="stylesheet">
<style>
:root{
  --blue-deep:#0555a3;
  --blue-nav:#3176b5;
  --blue-soft:#85acd3;
  --grey-mid:#5c5c5c;
  --grey-dark:#474747;
  --page-bg:#eef1f5;
  --white:#ffffff;
  --ink:#111111;
  --body-ink:#333333;
}
*{margin:0;padding:0;box-sizing:border-box}
html,body{width:1200px;height:2206px;overflow:hidden}
body{position:relative;background:var(--page-bg);font-family:"Arimo",Arial,sans-serif;color:var(--body-ink)}
.abs{position:absolute}

/* navigation */
.top-nav{left:0;top:0;width:1200px;height:48px;background:var(--blue-nav)}
.top-nav a{position:absolute;top:0;height:48px;line-height:48px;font-family:"Tinos",serif;font-size:18px;color:var(--white);text-decoration:none;text-align:center}
.top-nav a.active{background:var(--white);color:var(--ink);width:88px}

/* header */
.site-header{left:0;top:48px;width:1200px;height:156px;background:var(--white)}
.brand{left:34px;top:46px;display:flex;align-items:center;gap:14px}
.brand-mark{width:22px;height:22px;background:var(--blue-deep)}
.brand-name{font-family:"Arimo",sans-serif;font-weight:700;font-size:24px;line-height:28px;color:var(--blue-deep);letter-spacing:1px}

/* hero */
.hero{left:0;top:204px;width:1200px;height:628px;
  background:
   radial-gradient(ellipse 420px 300px at 560px 520px,#8a6a3a 0%,rgba(138,106,58,0) 70%),
   radial-gradient(ellipse 380px 360px at 1050px 200px,#4d6b2c 0%,rgba(77,107,44,0) 75%),
   radial-gradient(ellipse 360px 380px at 140px 160px,#3f5a26 0%,rgba(63,90,38,0) 75%),
   linear-gradient(180deg,#c9d6e2 0%,#a9b8a3 55%,#5e7a3e 100%)}
.hero-kicker{left:34px;top:291px;font-size:20px;color:var(--white)}
.hero-title{left:34px;top:320px;width:420px;font-family:"Tinos",serif;font-size:29px;line-height:37px;color:var(--white)}
.hero-text{left:34px;top:458px;width:380px;font-size:17px;line-height:25px;color:var(--white)}
.hero-btn{left:35px;top:569px;width:158px;height:53px;line-height:53px;text-align:center;background:var(--grey-dark);color:var(--white);font-size:17px;border-radius:3px}

/* services strip */
.services{left:57px;top:685px;width:1086px;height:147px;background:rgba(71,71,71,.78);display:flex}
.service{flex:1;position:relative;border-left:1px solid rgba(133,172,211,.6)}
.service:first-child{border-left:none}
.service svg{position:absolute;left:28px;top:26px}
.service h3{position:absolute;left:86px;top:24px;font-family:"Tinos",serif;font-weight:400;font-size:19px;line-height:25px;color:var(--white)}
.service p{position:absolute;left:86px;top:88px;font-size:17px;line-height:25px;color:var(--white)}

/* projects */
.projects{left:57px;top:878px;width:1086px;height:732px;background:var(--white)}
.pill{left:443px;top:125px;width:200px;height:37px;line-height:37px;text-align:center;background:var(--grey-mid);color:var(--white);font-size:13px;font-weight:700;border-radius:3px}
.section-title{left:0;top:210px;width:1086px;text-align:center;font-family:"Tinos",serif;font-weight:700;font-size:30px;color:var(--ink)}
.project{top:288px;width:228px}
.project-img{width:228px;height:115px;border:1px solid #777}
.project h3{margin-top:30px;font-size:20px;font-weight:700;color:var(--ink)}
.project p{margin-top:22px;font-size:15.5px;line-height:25px;color:var(--body-ink)}
.btn-outline{position:absolute;top:368px;left:0;width:147px;height:53px;line-height:51px;text-align:center;border:1px solid #8a8a8a;font-size:17px;color:var(--body-ink)}

/* footer */
.footer{left:57px;top:1610px;width:1086px;height:483px;background:var(--blue-deep)}
.footer h4{position:absolute;top:96px;font-size:17px;font-weight:700;color:var(--white)}
.footer p{position:absolute;font-size:15.5px;line-height:25px;color:var(--white)}
.footer-btn{position:absolute;left:50px;top:355px;width:159px;height:51px;line-height:49px;text-align:center;border:1.5px solid var(--white);color:var(--white);font-size:14px;font-weight:700}
.footer-brand{left:774px;top:94px;display:flex;align-items:center;gap:12px}
.footer-brand .brand-mark{width:18px;height:18px;background:var(--white)}
.footer-brand .brand-name{font-size:18px;line-height:22px;color:var(--white)}
.copyright{left:57px;top:2093px;width:1086px;height:113px;background:var(--grey-mid);color:var(--white);font-size:15.5px;padding:47px 0 0 50px}
</style>
</head>
<body>

<nav class="abs top-nav">
  <a class="active" style="left:118px">HOME</a>
  <a style="left:231px">SERVICES</a>
  <a style="left:354px">PROJECTS</a>
  <a style="left:482px">CONTACT</a>
</nav>

<header class="abs site-header">
  <div class="abs brand">
    <span class="brand-mark"></span>
    <span class="brand-name">CORVANE<br>REAL ESTATE MANAGEMENT</span>
  </div>
</header>

<section class="abs hero" role="img" aria-label="Photo of a two-storey suburban house with brown siding surrounded by tall green trees"></section>
<div class="abs hero-kicker">PROVIDING QUALITY</div>
<h1 class="abs hero-title" style="font-weight:400">COMMERCIAL AND MULTIFAMILY PORTFOLIO MANAGEMENT</h1>
<p class="abs hero-text">Sed ut perspiciatis unde omnis iste natus error sit voluptatem accusantium doloremque laudantium, totam rem aperiam.</p>
<div class="abs hero-btn">LEARN MORE</div>

<div class="abs services">
  <div class="service">
    <svg width="44" height="40" viewBox="0 0 44 40" fill="none" stroke="#fff" stroke-width="3">
      <rect x="3" y="8" width="30" height="20"/><path d="M18 28v7M10 36h16"/><path d="M24 20l14-14 4 4-14 14h-4z" fill="#fff"/>
    </svg>
    <h3>OFFICE<br>MANAGEMENT</h3>
    <p>Lorem ipsum dolor sit amet,<br>consectetur adipiscing elit.</p>
  </div>
  <div class="service">
    <svg width="44" height="40" viewBox="0 0 44 40" fill="none" stroke="#fff" stroke-width="2.5">
      <rect x="12" y="3" width="16" height="18"/><path d="M15 9h10M15 14h10"/><path d="M4 34a10 10 0 0 1 20 0z" fill="#fff"/><circle cx="33" cy="28" r="8"/><path d="M33 24v4h3"/>
    </svg>
    <h3>PORTFOLIO<br>MANAGEMENT</h3>
    <p>Lorem ipsum dolor sit amet,<br>consectetur adipiscing elit.</p>
  </div>
  <div class="service">
    <svg width="44" height="40" viewBox="0 0 44 40">
      <path d="M6 12h28v22H6z" fill="#fff"/><path d="M10 12l16-8 4 8" fill="#fff"/><rect x="26" y="19" width="10" height="8" rx="2" fill="#5c5c5c"/>
    </svg>
    <h3>FINANCIAL<br>MANAGEMENT</h3>
    <p>Lorem ipsum dolor sit amet,<br>consectetur adipiscing elit.</p>
  </div>
</div>

<main class="abs projects">
  <div class="abs pill">WHAT WE DO</div>
  <h2 class="abs section-title">OUR RECENT PROJECTS</h2>

  <article class="abs project" style="left:25px">
    <div class="project-img" role="img" aria-label="White apartment building with balconies" style="background:linear-gradient(180deg,#dfe6ee,#f4f4f2 55%,#9fa69a)"></div>
    <h3>PROJECT NAME</h3>
    <p>Lorem ipsum dolor sit amet, consectetur adipiscing elit, sed do eiusmod tempor incididunt ut labore et dolore magna aliqua.</p>
    <div class="btn-outline">READ MORE</div>
  </article>
  <article class="abs project" style="left:296px">
    <div class="project-img" role="img" aria-label="Stone cottage with red flowers in the garden" style="background:linear-gradient(180deg,#8fa8c4,#6b6a5e 50%,#5d8a3a 80%,#b23a32)"></div>
    <h3>PROJECT NAME</h3>
    <p>Lorem ipsum dolor sit amet, consectetur adipiscing elit, sed do eiusmod tempor incididunt ut labore et dolore magna aliqua.</p>
    <div class="btn-outline">READ MORE</div>
  </article>
  <article class="abs project" style="left:568px">
    <div class="project-img" role="img" aria-label="Calculator and pen on financial papers" style="background:linear-gradient(135deg,#d8d8d8,#8a8a8a 45%,#303030 60%,#cfcfcf)"></div>
    <h3>PROJECT NAME</h3>
    <p>Lorem ipsum dolor sit amet, consectetur adipiscing elit, sed do eiusmod tempor incididunt ut labore et dolore magna aliqua.</p>
    <div class="btn-outline">READ MORE</div>
  </article>
  <article class="abs project" style="left:839px">
    <div class="project-img" role="img" aria-label="Brick office building behind green leaves" style="background:linear-gradient(90deg,#3f6e2c,#7aa35a 40%,#c9a88a 65%,#d9c7b2)"></div>
    <h3>PROJECT NAME</h3>
    <p>Lorem ipsum dolor sit amet, consectetur adipiscing elit, sed do eiusmod tempor incididunt ut labore et dolore magna aliqua.</p>
    <div class="btn-outline">READ MORE</div>
  </article>
</main>

<footer class="abs footer">
  <h4 style="left:50px">ABOUT US</h4>
  <p style="left:50px;top:166px;width:260px">Sed ut perspiciatis unde omnis iste natus error sit voluptatem accusantium doloremque laudantium, totam rem aperiam, eaque ipsa quae ab illo inventore veritatis et quasi architecto.</p>
  <div class="footer-btn">LEARN MORE</div>

  <h4 style="left:411px">CONTACT</h4>
  <p style="left:411px;top:166px;width:270px">ADDRESS: Name of Street, Name of State</p>
  <p style="left:411px;top:241px">PHONE:999-999-999</p>

  <div class="abs footer-brand">
    <span class="brand-mark"></span>
    <span class="brand-name">CORVANE<br>REAL ESTATE MANAGEMENT</span>
  </div>
</footer>

<div class="abs copyright">Copyright © 2017 Corvane Real Estate Management</div>

</body>
</html>
```